Vitamin/Dietary Supplement Company needs a simple Hemp CBD Health retail website to display a few...

We need a simple website designed that will allow us to display a few products for purchase. We are a vitamin/dietary supplement company that wants to set up a separate website for CBD health products. CBD is a chemical compound found in hemp and cannabis plants that provide various health and medicinal benefits. Our target audience are individuals that suffer from health issues and would like to treat their pain relief with CBD as an alternative to prescription medication and over the counter drugs such as Paxorin and Dolvex. Looking for a simple and clean website that is easy for customers to navigate and purchase products.

Need extra days to review

Target Market(s)

Our target audience are individuals that suffer from health issues and would like to treat their pain relief with CBD as an alternative to prescription medication and over the counter drugs such as Paxorin and Dolvex.

Coding

Coded - Design and coding required

Font styles to use
Serif

Colors

Designer to choose colors to be used in the design.

Requirements
Nice to have
• Homepage, About page, FAQ page, Contact page, Blog page

```html
<!DOCTYPE html>
<html lang="en">
<head>
<meta charset="utf-8">
<title>Hempwell — CBD Extracts</title>
<link href="https://fonts.googleapis.com/css2?family=Raleway:wght@500;600;700;800&family=Open+Sans:wght@400;600;700&display=swap" rel="stylesheet">
<style>
:root{
  --green:#3fae2a;
  --green-dark:#2f8d1e;
  --ink:#1f1f1f;
  --text:#444;
  --muted:#777;
  --light:#f1f1f1;
  --footer:#262626;
  --footer-deep:#1b1b1b;
  --white:#fff;
}
*{box-sizing:border-box;margin:0;padding:0}
html,body{width:1200px;height:3888px;overflow:hidden}
body{font-family:"Open Sans",Arial,sans-serif;color:var(--text);background:var(--white);position:relative}
.wrap{width:920px;margin:0 auto;position:relative}
.section-title{font-family:"Raleway",Arial,sans-serif;font-weight:700;font-size:34px;letter-spacing:1px;color:var(--ink);text-align:center;text-transform:uppercase}
.section-title span{color:var(--green)}
.divider{width:280px;height:2px;background:#333;margin:22px auto 0;position:relative}
.divider::after{content:"";position:absolute;left:50%;top:50%;width:22px;height:22px;border-radius:50%;background:var(--green);transform:translate(-50%,-50%);box-shadow:0 0 0 4px var(--white)}
.btn{display:inline-block;background:var(--green);color:var(--white);font-family:"Raleway",Arial,sans-serif;font-weight:700;font-size:13px;text-transform:uppercase;border-radius:20px;padding:8px 22px;border:2px solid #d9f0d3}

/* header */
.topbar{position:absolute;top:0;left:0;width:1200px;height:36px;background:#1a3312;color:#fff;font-size:12px;z-index:3}
.topbar .wrap{display:flex;justify-content:space-between;align-items:center;height:36px}
.topbar .contacts span{margin-right:22px}
.navbar{position:absolute;top:36px;left:0;width:1200px;height:64px;background:var(--white);z-index:3}
.navbar .wrap{display:flex;align-items:center;justify-content:space-between;height:64px}
.brand{font-family:"Raleway",Arial,sans-serif;font-weight:800;font-size:28px;color:var(--green-dark);display:flex;align-items:center;gap:10px}
.brand i{width:18px;height:18px;border-radius:50%;background:var(--green);display:block}
.menu{display:flex;gap:30px;align-items:center;font-family:"Raleway",Arial,sans-serif;font-weight:700;font-size:13px;color:var(--ink);text-transform:uppercase}
.menu .active{color:var(--green)}

/* hero */
.hero{position:absolute;top:100px;left:0;width:1200px;height:545px;background:radial-gradient(ellipse at 50% 40%,#8aa860 0%,#4e7a33 45%,#2d4d1f 80%);}
.hero-content{position:absolute;top:165px;left:0;width:1200px;text-align:center;color:#fff}
.hero h1{font-family:"Raleway",Arial,sans-serif;font-weight:800;font-size:64px;letter-spacing:2px}
.hero p{width:620px;margin:12px auto 28px;font-size:14px;line-height:1.6}
.features{position:absolute;top:520px;left:0;width:1200px;z-index:2}
.feature{position:absolute;width:226px;height:210px;background:var(--white);box-shadow:0 4px 14px rgba(0,0,0,.15);text-align:center;padding-top:30px;border-bottom:3px solid #333}
.feature .ico{width:56px;height:56px;border-radius:50%;background:var(--green);margin:0 auto 18px;display:flex;align-items:center;justify-content:center}
.feature h3{font-family:"Raleway",Arial,sans-serif;font-weight:700;font-size:17px;color:var(--green);text-transform:uppercase;margin-bottom:10px}
.feature p{font-size:12.5px;line-height:1.55;padding:0 22px;color:var(--text)}

/* about */
.about{position:absolute;top:790px;left:0;width:1200px;text-align:center}
.about p{width:860px;margin:36px auto 26px;font-size:14px;line-height:2}

/* products */
.products{position:absolute;top:1085px;left:0;width:1200px;height:640px;background:var(--light)}
.products .section-title{margin-top:64px}
.product-row{position:absolute;top:175px;left:140px;width:920px;display:flex;justify-content:space-between}
.product{width:196px;text-align:center}
.product .photo{height:250px;background:linear-gradient(180deg,#e9e9e9,#d7d7d7);border-radius:4px}
.product h4{font-family:"Raleway",Arial,sans-serif;font-weight:700;font-size:16px;color:var(--green);text-transform:uppercase;margin:16px 0 6px}
.product p{font-size:11.5px;line-height:1.5;color:var(--text)}
.buy{display:flex;justify-content:center;margin-top:16px}
.price{border:1px solid #bbb;background:#fff;font-weight:700;font-size:15px;color:var(--ink);padding:6px 14px}
.shop{background:var(--green);color:#fff;font-weight:700;font-size:11px;padding:9px 12px;text-transform:uppercase}
.arrow{position:absolute;top:300px;width:28px;height:28px;border-radius:50%;display:flex;align-items:center;justify-content:center}
.arrow.prev{left:138px;background:var(--green)}
.arrow.next{left:1030px;background:#222}

/* benefits */
.benefits{position:absolute;top:1780px;left:0;width:1200px;height:620px}
.benefits .bottle{position:absolute;left:470px;top:130px;width:260px;height:430px;background:linear-gradient(180deg,#4a3a2c,#2b2019);border-radius:16px}
.benefit{position:absolute;width:330px;display:flex;gap:16px;align-items:flex-start}
.benefit.left{left:140px;text-align:right;flex-direction:row-reverse}
.benefit.right{left:780px}
.benefit .b-ico{flex:0 0 50px;height:50px;display:flex;align-items:center;justify-content:center}
.benefit h5{font-family:"Raleway",Arial,sans-serif;font-weight:700;font-size:19px;color:var(--green);margin-bottom:6px}
.benefit p{font-size:12.5px;line-height:1.55;color:var(--text)}
.benefit .txt{width:260px}

/* quality */
.quality{position:absolute;top:2415px;left:0;width:1200px;height:425px;background:linear-gradient(90deg,#efefef 0%,#eaeaea 45%,#d8cfae 100%)}
.quality .photo{position:absolute;right:0;top:0;width:640px;height:425px;background:linear-gradient(90deg,rgba(234,234,234,1) 0%,rgba(200,180,120,.55) 40%,#a0893d 75%,#6e7a3a 100%)}
.quality .copy{position:absolute;left:142px;top:92px;width:500px}
.quality h2{font-family:"Raleway",Arial,sans-serif;font-weight:800;font-size:32px;color:var(--ink);text-transform:uppercase;letter-spacing:1px}
.quality h2 span{color:var(--green)}
.quality .divider{margin:20px 0 0;width:190px}
.quality .divider::after{left:100px;box-shadow:0 0 0 4px #eee}
.quality p{font-size:14px;line-height:1.9;margin-top:30px}

/* blog */
.blog{position:absolute;top:2885px;left:0;width:1200px;height:500px}
.blog-row{position:absolute;top:135px;left:190px;width:820px;display:flex;justify-content:space-between}
.post{width:262px;box-shadow:0 2px 10px rgba(0,0,0,.12);background:#fff;padding-bottom:20px}
.post .photo{height:160px;position:relative}
.post .date{position:absolute;left:0;top:0;background:var(--green);color:#fff;font-family:"Raleway",Arial,sans-serif;font-weight:800;font-size:14px;line-height:1.2;padding:8px 12px;text-align:left;text-transform:uppercase}
.post h6{font-family:"Open Sans",Arial,sans-serif;font-weight:700;font-size:13px;color:var(--ink);line-height:1.5;padding:18px 16px 12px}
.post p{font-size:12px;line-height:1.55;padding:0 16px;color:var(--muted)}
.blog .arrow{top:340px;width:22px;height:22px;border:1px solid #999;background:#fff}
.blog .arrow.prev{left:140px}
.blog .arrow.next{left:1030px}

/* newsletter */
.newsletter{position:absolute;top:3405px;left:0;width:1200px;height:186px;background:var(--green)}
.newsletter .copy{position:absolute;left:142px;top:30px;color:#fff}
.newsletter h3{font-family:"Raleway",Arial,sans-serif;font-weight:800;font-size:24px;text-transform:uppercase;letter-spacing:.5px}
.newsletter p{font-size:13px;margin:6px 0 18px}
.signup{display:flex}
.signup .field{width:455px;height:36px;background:#fff;font-size:12px;color:#666;padding:10px 12px}
.signup .go{background:#111;color:#fff;font-weight:700;font-size:13px;padding:10px 20px;text-transform:uppercase}
.newsletter .photo{position:absolute;right:120px;top:-28px;width:260px;height:214px;background:radial-gradient(ellipse at 60% 55%,#e8cf7a 0%,#a8c58c 45%,rgba(63,174,42,0) 75%)}

/* footer */
.footer{position:absolute;top:3591px;left:0;width:1200px;height:260px;background:var(--footer);color:#ddd}
.cols{position:absolute;top:40px;left:142px;width:920px;display:flex;justify-content:space-between}
.col h4{font-family:"Raleway",Arial,sans-serif;font-weight:800;font-size:15px;color:var(--green);text-transform:uppercase;margin-bottom:14px}
.col ul{list-style:none}
.col li{font-size:11px;text-transform:uppercase;line-height:2.45;display:flex;align-items:center;gap:10px}
.col li::before{content:"";width:5px;height:5px;background:var(--green);border-radius:50%}
.col.contact li{text-transform:none;font-size:12px;line-height:1.6;align-items:flex-start;margin-bottom:12px}
.col.contact li::before{display:none}
.pays{display:flex;gap:6px;margin-top:4px}
.pays i{width:34px;height:22px;border-radius:3px;background:#dcdcdc;display:block}
.pays i:nth-child(2){background:#c9c9c9}
.pays i:nth-child(3){background:#bfd3e6}
.socials{display:flex;gap:12px;margin-top:6px;padding-left:28px}
.socials i{width:12px;height:12px;border-radius:50%;background:var(--green);display:block}
.copyright{position:absolute;top:3851px;left:0;width:1200px;height:37px;background:var(--footer-deep);color:#bbb;font-size:11px;text-align:center;line-height:37px}
</style>
</head>
<body>

<header>
  <div class="topbar">
    <div class="wrap">
      <div class="contacts"><span>&#9742; +123 555 0147</span><span>&#9993; info@hempwellcare.com</span></div>
      <div>&#9679; LOGIN | REGISTER &nbsp;&nbsp; &#128722; 0</div>
    </div>
  </div>
  <nav class="navbar">
    <div class="wrap">
      <div class="brand">HEMPWELL <i></i></div>
      <div class="menu">
        <span class="active">Home</span><span>About Us</span><span>Quality Control</span><span>Blog</span><span>FAQ</span><span>Contact Us</span>
        <span class="btn">Shop Now</span>
      </div>
    </div>
  </nav>
</header>

<section class="hero" role="img" aria-label="Close-up photo of green hemp leaves in soft sunlight">
  <div class="hero-content">
    <h1>CDB EXTRACTS</h1>
    <p>Lorem ipsum dolor sit amet, consectetuer adipiscing elit, sed diam nonummy nibh euismod tincidunt ut laoreet dolore magna aliquam erat volutpat.</p>
    <span class="btn">Shop Now</span>
  </div>
</section>

<div class="features">
  <div class="feature" style="left:142px">
    <div class="ico"><svg width="24" height="28" viewBox="0 0 24 28"><path d="M12 2 C12 2 3 13 3 18 a9 9 0 0 0 18 0 C21 13 12 2 12 2z" fill="#fff"/></svg></div>
    <h3>About CBD</h3>
    <p>Lorem ipsum dolor sit amet, consectetuer adipiscing elit, sed diam nonummy nibh</p>
  </div>
  <div class="feature" style="left:488px">
    <div class="ico"><svg width="28" height="26" viewBox="0 0 28 26"><path d="M14 24 L3 13 a6 6 0 0 1 11-8 a6 6 0 0 1 11 8z" fill="#fff"/></svg></div>
    <h3>Advantages of CBD</h3>
    <p>Lorem ipsum dolor sit amet, consectetuer adipiscing elit, sed diam nonummy nibh</p>
  </div>
  <div class="feature" style="left:835px">
    <div class="ico"><svg width="28" height="26" viewBox="0 0 28 26"><path d="M2 3h5l3 13h13l3-9H9" fill="none" stroke="#fff" stroke-width="2.5"/><circle cx="11" cy="22" r="2.2" fill="#fff"/><circle cx="21" cy="22" r="2.2" fill="#fff"/></svg></div>
    <h3>Buy CBD</h3>
    <p>Lorem ipsum dolor sit amet, consectetuer adipiscing elit, sed diam nonummy nibh</p>
  </div>
</div>

<section class="about">
  <h2 class="section-title">About <span>Hempwell</span></h2>
  <div class="divider"></div>
  <p>Lorem ipsum dolor sit amet, consectetuer adipiscing elit, sed diam nonummy nibh euismod tincidunt ut laoreet dolore magna aliquam erat volutpat. Ut wisi enim ad minim veniam, quis nostrud exerci tation ullamcorper suscipit lobortis nisl ut aliquip ex ea commodo consequat. Duis autem vel eum iriure dolor in hendrerit in vulputate velit esse molestie consequat.</p>
  <span class="btn">Read More</span>
</section>

<section class="products">
  <h2 class="section-title">Our <span>Product</span></h2>
  <div class="divider" style="box-shadow:none"></div>
  <div class="arrow prev"><svg width="10" height="12"><path d="M8 1 L2 6 L8 11" stroke="#fff" stroke-width="2" fill="none"/></svg></div>
  <div class="arrow next"><svg width="10" height="12"><path d="M2 1 L8 6 L2 11" stroke="#fff" stroke-width="2" fill="none"/></svg></div>
  <div class="product-row">
    <div class="product"><div class="photo" role="img" aria-label="Amber pump bottle of classic CBD oil"></div><h4>Classic</h4><p>240mg Full Spectrum CBD Oil,<br>High Grade Hemp Extract<br>(10mg/ml)</p><div class="buy"><span class="price">$ 38.50</span><span class="shop">Shop Now</span></div></div>
    <div class="product"><div class="photo" role="img" aria-label="Amber pump bottle of signature CBD oil"></div><h4>Signature</h4><p>720mg Full Spectrum CBD Oil,<br>High Grade Hemp Extract<br>(30mg/ml)</p><div class="buy"><span class="price">$ 99.00</span><span class="shop">Shop Now</span></div></div>
    <div class="product"><div class="photo" role="img" aria-label="Amber pump bottle of classic CBD oil"></div><h4>Classic</h4><p>240mg Full Spectrum CBD Oil,<br>High Grade Hemp Extract<br>(10mg/ml)</p><div class="buy"><span class="price">$ 38.50</span><span class="shop">Shop Now</span></div></div>
    <div class="product"><div class="photo" role="img" aria-label="Amber pump bottle of signature CBD oil"></div><h4>Signature</h4><p>720mg Full Spectrum CBD Oil,<br>High Grade Hemp Extract<br>(30mg/ml)</p><div class="buy"><span class="price">$ 99.00</span><span class="shop">Shop Now</span></div></div>
  </div>
</section>

<section class="benefits">
  <h2 class="section-title">Hempwell <span>Products Benifits</span></h2>
  <div class="divider"></div>
  <div class="bottle" role="img" aria-label="Large amber pump bottle of CBD oil with hemp leaves"></div>

  <div class="benefit left" style="top:180px"><div class="b-ico"><svg width="40" height="40" viewBox="0 0 40 40"><path d="M6 20 L20 8 L34 20 V34 H6z" fill="none" stroke="#3fae2a" stroke-width="2"/></svg></div><div class="txt"><h5>Anxiety Relief</h5><p>Pesticide free and Non - GMO</p></div></div>
  <div class="benefit left" style="top:300px"><div class="b-ico"><svg width="40" height="40" viewBox="0 0 40 40"><circle cx="20" cy="20" r="14" fill="#3fae2a"/></svg></div><div class="txt"><h5>Anti-seizure</h5><p>Made in the USA 3rd party<br>tested, gluten free</p></div></div>
  <div class="benefit left" style="top:420px"><div class="b-ico"><svg width="40" height="40" viewBox="0 0 40 40"><path d="M20 4 L34 9 V20 C34 29 27 34 20 36 C13 34 6 29 6 20 V9z" fill="none" stroke="#3fae2a" stroke-width="2"/><path d="M13 20 L18 25 L27 15" fill="none" stroke="#3fae2a" stroke-width="2.5"/></svg></div><div class="txt"><h5>Third-Party Verified</h5><p>Made in the USA 3rd party<br>tested, gluten free</p></div></div>

  <div class="benefit right" style="top:180px"><div class="b-ico"><svg width="40" height="40" viewBox="0 0 40 40"><rect x="12" y="6" width="16" height="30" rx="3" fill="none" stroke="#3fae2a" stroke-width="2"/></svg></div><div class="txt"><h5>Pain Relief</h5><p>Low carbon footprint, that's<br>why we buy local, reuse</p></div></div>
  <div class="benefit right" style="top:300px"><div class="b-ico"><svg width="40" height="40" viewBox="0 0 40 40"><circle cx="20" cy="20" r="13" fill="none" stroke="#3fae2a" stroke-width="2"/><path d="M20 13 V27 M13 20 H27" stroke="#3fae2a" stroke-width="2"/></svg></div><div class="txt"><h5>Cancer Treatment</h5><p>Pesticides Free, No metals, No<br>harsh chemicals and zero THC.</p></div></div>
  <div class="benefit right" style="top:420px"><div class="b-ico"><svg width="40" height="40" viewBox="0 0 40 40"><path d="M16 6 H24 M18 6 V16 L10 32 H30 L22 16 V6" fill="none" stroke="#3fae2a" stroke-width="2"/></svg></div><div class="txt"><h5>Green Extraction Methods</h5><p>Pesticides Free, No metals, No<br>harsh chemicals and zero THC.</p></div></div>
</section>

<section class="quality">
  <div class="photo" role="img" aria-label="Glass jars of golden CBD oil beside dried hemp buds on a wooden table"></div>
  <div class="copy">
    <h2>Quality <span>Control</span></h2>
    <div class="divider"></div>
    <p>Lorem ipsum dolor sit amet, consectetuer adipiscing elit, sed diam nonummy nibh euismod tincidunt ut laoreet dolore magna aliquam erat volutpat. Ut wisi enim ad minim veniam,</p>
    <p style="margin-top:22px">quis nostrud exerci tation ullamcorper suscipit lobortis nisl ut aliquip ex ea commodo consequat. Duis autem vel eum iriure dolor in hendrerit in vulputate velit esse molestie consequat.</p>
  </div>
</section>

<section class="blog">
  <h2 class="section-title">Latest <span>Blog</span></h2>
  <div class="divider"></div>
  <div class="arrow prev"><svg width="8" height="10"><path d="M6 1 L2 5 L6 9" stroke="#555" stroke-width="1.5" fill="none"/></svg></div>
  <div class="arrow next"><svg width="8" height="10"><path d="M2 1 L6 5 L2 9" stroke="#555" stroke-width="1.5" fill="none"/></svg></div>
  <div class="blog-row">
    <article class="post"><div class="photo" role="img" aria-label="Hands tending hemp plants in a field" style="background:linear-gradient(135deg,#7da85a,#3f6a2c)"><div class="date">10<br>July</div></div><h6>Lorem ipsum dolor sit amet, consectetuer Lorem ipsumconse</h6><p>Lorem ipsum dolor sit amet, consectetuer adipiscing elit, sed diam nonummy nibh euismod tincidunt ut laoreet dolore magna aliquam erat volut, consectetuer</p></article>
    <article class="post"><div class="photo" role="img" aria-label="Young hemp seedling growing in soil at sunset" style="background:linear-gradient(135deg,#d7a24a,#5a4a22)"><div class="date">13<br>Aug</div></div><h6>Lorem ipsum dolor sit amet, consectetuer Lorem ipsumconse</h6><p>Lorem ipsum dolor sit amet, consectetuer adipiscing elit, sed diam nonummy nibh euismod tincidunt ut laoreet dolore magna aliquam erat volut, consectetuer</p></article>
    <article class="post"><div class="photo" role="img" aria-label="Gloved hand holding a dropper bottle beside a hemp leaf" style="background:linear-gradient(135deg,#e7e7ea,#5a5fc0)"><div class="date">16<br>Aug</div></div><h6>Lorem ipsum dolor sit amet, consectetuer Lorem ipsumconse</h6><p>Lorem ipsum dolor sit amet, consectetuer adipiscing elit, sed diam nonummy nibh euismod tincidunt ut laoreet dolore magna aliquam erat volut, consectetuer</p></article>
  </div>
</section>

<section class="newsletter">
  <div class="photo" role="img" aria-label="Small glass bottle of CBD oil with hemp leaves"></div>
  <div class="copy">
    <h3>Signup for our Newsletter</h3>
    <p>Get the latest updates by entering your email address</p>
    <div class="signup"><span class="field">Email Address</span><span class="go">Subscribe</span></div>
  </div>
</section>

<footer class="footer">
  <div class="cols">
    <div class="col"><h4>Quick Links</h4><ul><li>Home</li><li>About Us</li><li>Quality Control</li><li>Blog</li><li>FAQ</li><li>Contact Us</li></ul></div>
    <div class="col"><h4>Can We Help You ?</h4><ul><li>Your Account</li><li>Shipping &amp; Handling</li><li>Refunds &amp; Returns</li><li>Stockists</li><li>Privacy Policy</li><li>Terms &amp; Conditions</li><li>Sitemap</li></ul></div>
    <div class="col"><h4>Shipping &amp; Returns</h4><ul><li>Standard Return Policy</li><li>Shipping Policy</li><li>Delivery Policies</li></ul>
      <h4 style="margin-top:34px">Payment Options</h4><div class="pays"><i></i><i></i><i></i><i></i></div></div>
    <div class="col contact"><h4>Contact Details</h4><ul>
      <li><svg width="14" height="16" viewBox="0 0 14 16"><path d="M7 1a5 5 0 0 0-5 5c0 4 5 9 5 9s5-5 5-9a5 5 0 0 0-5-5z" fill="#3fae2a"/></svg>2140 Meadow Lane #4B<br>Riverton, CO 80123</li>
      <li><svg width="14" height="14" viewBox="0 0 14 14"><path d="M3 1l3 3-2 2c1 2 2 3 4 4l2-2 3 3-2 2C6 13 1 8 1 3z" fill="#3fae2a"/></svg>+123 555 0147</li>
      <li><svg width="14" height="12" viewBox="0 0 14 12"><rect x="1" y="1" width="12" height="10" fill="#3fae2a"/><path d="M1 1l6 5 6-5" stroke="#262626" fill="none"/></svg>info@hempwellcare.com</li>
    </ul><div class="socials"><i></i><i></i><i></i><i></i></div></div>
  </div>
</footer>
<div class="copyright">© Copyrights 2018 Hempwell Care. All rights reserved.</div>

</body>
</html>
```